I need a very simple web page/site for my business

I have recently commissioned a logo and letterhead, I simply need someone to design a webpage/site that builds on this with a creative design and places for page titles along with descriptions of the services I offer on each page and contact details etc. I would imagine a cover page with two to three sub-pages at the most. i.e. a Home page, then "About As", "Services Offered" and "Contact and Support" pages. The Red on White design is the primary one while the Red on Black one can be used secondarily or at the bottom of pages etc, however the designer thinks best. The design should convey professionalism, technical expertise, and timeliness from a number of suitably qualified medical practitioners. If need be I can provide the necessary text, otherwise an option that allows me to fill this in afterwards would be ideal. I am not sure of the practicality of that. The principal type of work done will be clinical analysis and report writing involving clinical trials, and clinical data that support the use of drugs and medical devices in humans. Also any consultation work that requires medical analysis and critique and formal report writing, such as safety analysis, clinical trial design, or essentially anything for which expert medical commentary is required.

```html
<!DOCTYPE html>
<html lang="en">
<head>
<meta charset="utf-8">
<title>Veritas Clinical Review</title>
<link href="https://fonts.googleapis.com/css2?family=Roboto:wght@300;400;500&display=swap" rel="stylesheet">
<style>
:root{
  --red:#c1272d;
  --red-dark:#a51f25;
  --blue:#2f9fd8;
  --text:#7a7a7a;
  --heading:#444;
  --line:#e4e4e4;
  --bg:#eeeeee;
  --footer:#2f2f2f;
  --footer-bar:#252525;
  --white:#fff;
}
*{box-sizing:border-box;margin:0;padding:0}
html,body{width:1200px;height:2509px;overflow:hidden}
body{background:var(--bg);font-family:'Roboto',Arial,sans-serif;color:var(--text);font-size:12px;position:relative}
.page{position:absolute;left:161px;top:0;width:878px;height:2487px;background:var(--white)}
.abs{position:absolute}
a{color:inherit;text-decoration:none}
ul{list-style:none}

/* header */
.brand{left:21px;top:30px;display:flex;align-items:center;gap:10px}
.brand-mark{width:22px;height:22px;background:var(--red)}
.brand-name{font-size:30px;font-weight:500;color:var(--red);letter-spacing:2px;line-height:1}
.brand-sub{left:53px;top:66px;font-size:9px;color:var(--text);letter-spacing:1px}
.contact-top{right:21px;top:36px;display:flex;gap:22px;font-size:11px;color:#555}
.contact-top span{display:flex;align-items:center;gap:6px}
.social-top{right:21px;top:70px;display:flex;gap:5px}
.social-top i{display:block;width:16px;height:16px;border:1px solid #ccc}
.social-top i.active{background:var(--red);border-color:var(--red)}

/* nav */
.nav{left:21px;top:115px;width:836px;height:40px;border-top:1px solid var(--line);border-bottom:1px solid var(--line);display:flex}
.nav a{height:38px;padding:0 22px;display:flex;align-items:center;font-size:10px;color:#555;border-right:1px solid var(--line);letter-spacing:.5px}
.nav a.current{background:var(--red);color:var(--white)}
.nav .search{margin-left:auto;border-right:0;border-left:1px solid var(--line);padding:0 14px}

/* hero */
.hero-title{left:66px;top:238px;font-size:44px;font-weight:300;color:var(--red);line-height:1}
.hero-sub{left:66px;top:287px;font-size:30px;font-weight:300;color:#555}
.hero-list{left:90px;top:362px;font-size:13px;letter-spacing:1.5px;line-height:26px;color:#8a8a8a}
.hero-list li:nth-child(2){color:#6a6a6a}
.hero-list li:nth-child(3){color:#aaa}
.hero-image{left:320px;top:190px;width:540px;height:418px;background:linear-gradient(100deg,#eef6fb 0%,#cfe3ef 45%,#eef3f6 80%,#fff 100%)}

/* info band */
.band{left:21px;top:610px;width:836px;height:193px;display:flex;background:var(--red);color:var(--white)}
.band-col{width:209px;padding:20px 16px}
.band-col h3{font-size:25px;font-weight:300;margin-bottom:20px;white-space:nowrap;line-height:30px}
.band-col p{font-size:11px;line-height:15px;height:60px;overflow:hidden}
.band-col .more{display:block;margin-top:20px;font-size:11px}
.band-col.hours{background:var(--red-dark);padding:20px 0 0;position:relative}
.hours h3{padding:0 16px;margin-bottom:12px}
.hours li{display:flex;justify-content:space-between;padding:0 16px;font-size:11px;height:28px;line-height:28px;border-bottom:1px solid rgba(255,255,255,.35)}
.hours .bar{position:absolute;left:0;bottom:0;width:100%;height:26px;background:var(--blue)}

/* intro */
.intro{left:0;top:836px;width:878px;text-align:center}
.intro h2{font-size:28px;font-weight:300;color:var(--blue)}
.intro p{font-size:14px;color:#999;margin-top:4px}
.features{left:21px;top:946px;width:836px;display:flex}
.feature{width:209px;text-align:center;padding:0 14px}
.feature svg{display:block;margin:0 auto 10px}
.feature h4{font-size:16px;font-weight:300;color:#555;margin-bottom:10px}
.feature p{font-size:10px;line-height:14px}

/* section headings */
.section-title{position:absolute;font-size:17px;font-weight:400;color:#555;padding-bottom:10px;white-space:nowrap}
.section-title::after{content:"";position:absolute;left:0;bottom:0;width:72px;height:2px;background:var(--red)}
.pager{display:flex;gap:2px}
.pager i{width:16px;height:16px;border:1px solid #ddd;display:block}

/* cards */
.cards{left:21px;width:836px;display:flex;gap:33px}
.card{width:184px;border:1px solid var(--line)}
.card-img{height:137px}
.card-body{padding:8px 12px}
.card-body h5{font-size:12px;font-weight:400;color:#555}
.card-body span{font-size:10px;color:var(--red)}
.card-social{display:flex;gap:10px;padding:8px 12px;border-top:1px solid var(--line)}
.card-social i{display:block;width:10px;height:10px;background:#bbb}
.card-social i:first-child{background:var(--red)}

/* news & testimonial */
.news-item{display:flex;gap:20px;width:410px;margin-bottom:16px}
.news-img{width:94px;height:94px;flex:none}
.news-item h5{font-size:14px;font-weight:400;color:var(--blue);margin-bottom:4px}
.news-meta{font-size:9px;color:#aaa;margin-bottom:8px}
.news-meta b{color:var(--red);font-weight:400}
.news-item p{font-size:10px;line-height:14px}
.quote{left:455px;top:1446px;width:401px;height:134px;border:1px solid var(--line);padding:18px 18px 18px 70px;font-size:11px;line-height:16px}
.quote .mark{position:absolute;left:18px;top:18px;width:30px;height:30px;background:var(--red)}
.author{left:455px;top:1599px;display:flex;align-items:center;gap:14px;font-size:11px;color:#555}
.author-img{width:42px;height:42px}
.author small{display:block;color:var(--blue);font-size:10px}

/* tweet band */
.tweet{left:0;top:2065px;width:878px;height:50px;background:var(--red);color:var(--white);display:flex;align-items:center;padding:0 21px;font-size:11px}
.tweet .bird{width:16px;height:16px;background:var(--white);margin-right:40px}
.tweet u{margin-left:4px}
.tweet .pager{margin-left:auto}
.tweet .pager i{border-color:var(--white);background:var(--red-dark)}

/* footer */
.footer{left:0;top:2115px;width:878px;height:320px;background:var(--footer);color:#aaa;padding:30px 21px}
.footer-col{position:absolute;top:30px;width:200px}
.footer-col h4{font-size:16px;font-weight:300;color:var(--white);padding-bottom:10px;position:relative;margin-bottom:16px}
.footer-col h4::after{content:"";position:absolute;left:0;bottom:0;width:40px;height:2px;background:var(--red)}
.footer-col p{font-size:10px;line-height:14px}
.footer-col li{font-size:10px;line-height:25px}
.footer-col li::before{content:"›";color:var(--red);margin-right:8px}
.contact-line{display:flex;gap:10px;font-size:10px;margin-top:16px;line-height:14px}
.contact-line i{width:8px;height:8px;border-radius:50%;background:var(--red);flex:none;margin-top:3px}
.form label{display:block;font-size:10px;margin-bottom:4px}
.form .field{height:22px;background:#3a3a3a;border:1px solid #444;margin-bottom:8px}
.form .area{height:86px}
.form .send{display:inline-block;background:var(--white);color:#333;font-size:10px;padding:6px 14px;margin-top:4px}
.footer-bar{left:0;top:2435px;width:878px;height:52px;background:var(--footer-bar);color:#888;font-size:10px;display:flex;align-items:center;padding:0 21px}
.footer-bar nav{margin-left:auto;display:flex;gap:14px}
</style>
</head>
<body>
<div class="page">

  <header>
    <div class="abs brand"><span class="brand-mark"></span><span class="brand-name">VERITAS</span></div>
    <div class="abs brand-sub">CLINICAL REVIEW</div>
    <div class="abs contact-top">
      <span><svg width="8" height="12" viewBox="0 0 8 12"><rect x="0.5" y="0.5" width="7" height="11" rx="1" fill="none" stroke="#c1272d"/></svg>Contact us: +44 20 7946 0321</span>
      <span><svg width="12" height="9" viewBox="0 0 12 9"><rect width="12" height="9" fill="#c1272d"/><path d="M0 0l6 5 6-5" stroke="#fff" fill="none"/></svg>hello@clinara.example</span>
    </div>
    <div class="abs social-top"><i class="active"></i><i></i><i></i><i></i><i></i></div>
  </header>

  <nav class="abs nav">
    <a class="current" href="#">HOME</a>
    <a href="#">FEATURES</a>
    <a href="#">SERVICES</a>
    <a href="#">DOCTORS</a>
    <a href="#">APPOINTMENTS</a>
    <a href="#">BLOG</a>
    <a href="#">CONTACTS</a>
    <a class="search" href="#"><svg width="14" height="14" viewBox="0 0 14 14"><circle cx="6" cy="6" r="4.5" fill="none" stroke="#c1272d" stroke-width="2"/><path d="M9.5 9.5L13 13" stroke="#c1272d" stroke-width="2"/></svg></a>
  </nav>

  <section class="hero">
    <h1 class="abs hero-title">Full Spectre</h1>
    <div class="abs hero-sub">Treatment</div>
    <ul class="abs hero-list"><li>Medical Counseling</li><li>Cardiac Clinyc</li><li>Pediatric Clinic</li></ul>
    <div class="abs hero-image" role="img" aria-label="Team of doctors in white coats and scrubs"></div>
  </section>

  <section class="abs band">
    <div class="band-col"><h3>Clinic News</h3><p>Clear reports on trial data and device safety, written by qualified physicians on an agreed timeline.</p><a class="more" href="#">Read More</a></div>
    <div class="band-col"><h3>Top Doctors</h3><p>Our panel brings senior clinical experience across cardiology, oncology and regulatory review.</p><a class="more" href="#">Read More</a></div>
    <div class="band-col"><h3>24 Hours Service</h3><p>Urgent safety questions receive prompt attention, with a reviewer on call for time critical requests.</p><a class="more" href="#">Read More</a></div>
    <div class="band-col hours">
      <h3>Opening Hours</h3>
      <ul><li><span>Monday - Friday</span><span>8.00 - 17.00</span></li><li><span>Saturday</span><span>9.30 - 17.30</span></li><li><span>Sunday</span><span>9.30 - 15.00</span></li></ul>
      <div class="bar"></div>
    </div>
  </section>

  <section class="abs intro">
    <h2>Awesome Theme for Medical and Health Websites</h2>
    <p>Clinara HTML theme was created to offer a perfect solution for medical websites.</p>
  </section>

  <section class="abs features">
    <div class="feature">
      <svg width="40" height="34" viewBox="0 0 40 34"><path d="M20 32S3 21 3 11a8 8 0 0 1 17-3 8 8 0 0 1 17 3c0 10-17 21-17 21z" fill="#2f9fd8"/><path d="M4 17h9l3-6 4 11 3-7h13" stroke="#fff" stroke-width="2" fill="none"/></svg>
      <h4>Cardio Monitoring</h4>
      <p>Structured review of cardiac endpoints and trial data, prepared with care by experienced physicians for sponsors.</p>
    </div>
    <div class="feature">
      <svg width="40" height="34" viewBox="0 0 40 34"><g transform="rotate(-45 20 17)"><rect x="6" y="10" width="28" height="14" rx="7" fill="none" stroke="#2f9fd8" stroke-width="3"/><path d="M20 10h7a7 7 0 0 1 0 14h-7z" fill="#2f9fd8"/></g></svg>
      <h4>Medical Treatment</h4>
      <p>A clear account of treatment outcomes, with plain commentary on risk, benefit and the strength of the evidence.</p>
    </div>
    <div class="feature">
      <svg width="40" height="34" viewBox="0 0 40 34"><rect x="14" y="3" width="12" height="6" fill="none" stroke="#2f9fd8" stroke-width="2"/><rect x="4" y="8" width="32" height="24" rx="2" fill="#2f9fd8"/><path d="M20 13v14M13 20h14" stroke="#fff" stroke-width="4"/></svg>
      <h4>Emergency Help</h4>
      <p>Safety signal analysis for drugs and devices, delivered as a formal written report ready for submission or audit.</p>
    </div>
    <div class="feature">
      <svg width="40" height="34" viewBox="0 0 40 34"><path d="M21 2a12 12 0 0 0-12 12l-4 6h4v6a3 3 0 0 0 3 3h5v4h12V22a12 12 0 0 0-8-20z" fill="#2f9fd8"/></svg>
      <h4>Emergency Help</h4>
      <p>Expert opinion on trial design, protocol choices and study populations, for a sponsor or a small research team.</p>
    </div>
  </section>

  <section>
    <h3 class="section-title" style="left:21px;top:1118px">Latest Services</h3>
    <div class="abs pager" style="left:823px;top:1122px"><i></i><i></i></div>
    <div class="abs cards" style="top:1171px">
      <article class="card"><div class="card-img" role="img" aria-label="Toddler at a pediatric check-up" style="background:linear-gradient(135deg,#f6e0d6,#e8c2b4)"></div><div class="card-body"><h5>Pediatric Clinic</h5><span>Pediatric, Therapy</span></div></article>
      <article class="card"><div class="card-img" role="img" aria-label="Doctor at a gynecological consultation" style="background:linear-gradient(135deg,#eef3f6,#c9dbe4)"></div><div class="card-body"><h5>Gynecological Clinic</h5><span>Therapy</span></div></article>
      <article class="card"><div class="card-img" role="img" aria-label="Laboratory glassware and samples" style="background:linear-gradient(135deg,#d4ecf2,#7ac0d6)"></div><div class="card-body"><h5>Laboratory Analysis</h5><span>Diagnosis, Pharmacy</span></div></article>
      <article class="card"><div class="card-img" role="img" aria-label="Doctors reviewing a cardiac case" style="background:linear-gradient(135deg,#e6eef4,#a9c6da)"></div><div class="card-body"><h5>Cardiac Clinic</h5><span>Diagnosis, Therapy</span></div></article>
    </div>
  </section>

  <section>
    <h3 class="section-title" style="left:21px;top:1392px">Latest News</h3>
    <div class="abs" style="left:21px;top:1446px">
      <article class="news-item"><div class="news-img" role="img" aria-label="Medical technology equipment" style="background:linear-gradient(135deg,#dbe8f0,#8fb6cf)"></div><div><h5>Center for Medical Technology Innovation</h5><div class="news-meta">January 24, 2014 &nbsp; Comments ( <b>0</b> )</div><p>Our team reviewed a new device study this month, with a report that covers safety, dosing and patient outcomes.</p></div></article>
      <article class="news-item"><div class="news-img" role="img" aria-label="Nutrition consultation with a patient" style="background:linear-gradient(135deg,#e3eef5,#9fc3db)"></div><div><h5>Nutritional Personal Consultation</h5><div class="news-meta">January 24, 2014 &nbsp; Comments ( <b>0</b> )</div><p>We can prepare a critique of any clinical protocol, and we keep the format flexible to suit each sponsor.</p></div></article>
    </div>

    <h3 class="section-title" style="left:455px;top:1392px">Testimonials</h3>
    <div class="abs pager" style="left:823px;top:1396px"><i></i><i></i></div>
    <blockquote class="abs quote"><span class="mark"></span>If you are choosing a medical center, Clinara is the one I would recommend. Here you are offered medical treatment of a reliable quality, and a full range of services is offered by a team of professional doctors. Caring staff, new equipment and helpful therapy - definitely, this is a medical center of my choice!</blockquote>
    <div class="abs author"><div class="author-img" role="img" aria-label="Portrait of the reviewer" style="background:linear-gradient(135deg,#e2d6cc,#b8a497)"></div><div>Aldous<small>57 years</small></div></div>
  </section>

  <section>
    <h3 class="section-title" style="left:21px;top:1676px">Our Doctors</h3>
    <div class="abs cards" style="top:1735px">
      <article class="card"><div class="card-img" role="img" aria-label="Portrait of a female doctor" style="height:184px;background:linear-gradient(180deg,#f2f4f6,#d4dde4)"></div><div class="card-body"><h5>Dr. Helen Marsh</h5><span style="color:var(--blue)">Pediatric Clinic</span></div><div class="card-social"><i></i><i></i><i></i></div></article>
      <article class="card"><div class="card-img" role="img" aria-label="Portrait of a senior doctor" style="height:184px;background:linear-gradient(180deg,#f2f4f6,#d4dde4)"></div><div class="card-body"><h5>Dr. Paul Reddy</h5><span style="color:var(--blue)">Cardiac Clinic</span></div><div class="card-social"><i></i><i></i><i></i></div></article>
      <article class="card"><div class="card-img" role="img" aria-label="Portrait of a male doctor" style="height:184px;background:linear-gradient(180deg,#f2f4f6,#d4dde4)"></div><div class="card-body"><h5>Dr. Omar Lindqvist</h5><span style="color:var(--blue)">Rehabilitation Therapy</span></div><div class="card-social"><i></i><i></i><i></i></div></article>
      <article class="card"><div class="card-img" role="img" aria-label="Portrait of a young doctor" style="height:184px;background:linear-gradient(180deg,#f2f4f6,#d4dde4)"></div><div class="card-body"><h5>Dr. Tom Ashby</h5><span style="color:var(--blue)">Laryngological Clinic</span></div><div class="card-social"><i></i><i></i><i></i></div></article>
    </div>
  </section>

  <div class="abs tweet"><span class="bird"></span>#Review We LOVE sharing GOOD reports... #Medical #Health #Clinara <u>clinara.example/news</u><div class="pager"><i></i><i></i></div></div>

  <footer class="abs footer">
    <div class="footer-col" style="left:21px">
      <h4>Clinara Information</h4>
      <p>Independent medical review of trial data and device safety, written by qualified clinicians.</p>
      <div class="contact-line"><i></i><span>Clinara Ltd<br><br>18 Harbour Row<br>Bristol<br>UK</span></div>
      <div class="contact-line"><i></i><span>(020) 7946 0188</span></div>
      <div class="contact-line"><i></i><span>hello@clinara.example</span></div>
    </div>
    <div class="footer-col" style="left:238px">
      <h4>Doctors</h4>
      <ul><li>Dr. Helen Marsh</li><li>Dr. Paul Reddy</li><li>Dr. Omar Lindqvist</li><li>Dr. Tom Ashby</li><li>Dr. Ravi Kohli</li><li>Dr. Lena Ortiz</li><li>Dr. Nora Flint</li></ul>
    </div>
    <div class="footer-col" style="left:455px">
      <h4>Services</h4>
      <ul><li>Pediatric Clinic</li><li>Diagnosis Clinic</li><li>Cardiac Clinic</li><li>Laboratory Analysis</li><li>Dental Clinic</li><li>Gynecological Clinic</li><li>Psychological Counseling</li></ul>
    </div>
    <div class="footer-col form" style="left:672px;width:185px">
      <h4>Quick Contacts</h4>
      <label>Your Email <span style="color:var(--red)">*</span></label><div class="field"></div>
      <label>Your message</label><div class="field area"></div>
      <span class="send">Submit</span>
    </div>
  </footer>

  <div class="abs footer-bar">Clinara © 2014 | All Rights Reserved<nav><a href="#">Home</a><a href="#">About Us</a><a href="#">Doctors</a><a href="#">Blog</a><a href="#">Contacts</a></nav></div>

</div>
</body>
</html>
```